Poster Design Project- kids dancing/sport

I need a poster design for a childrens dance and sport program!!
I have attached a brochure and logo designs. From the brochure please include information from sections titled "twirl'n'hop" and "themes". Also please put on the phone number and email address (found on the brochure). Emphasis on FUN!! Make poster colourful, very kid friendly and eye catching.
Some other things i would like on the poster are:
"Does your child love to dance, sing and play sport?? Why not enrol them in our fun-filled program?"
"From only $10.00 per class"
"Sign up for your FREE trial class today"
"A fun introduction to the joy of Dance, Sport and Music for 2-6yr olds. Held in your childcare centre!!"
Hi!!
I would like to stress its TRIAL class not TRAIL class. Please feel free to play around with the information, it doesnt need to be in one blurb. Also i have updated the brief. I would like "Does you child love to dance, sing or play sport? Why not enrol in our fun filled program?" or something to that effect!!
Thanks!!!!
2-6yr olds and their parents
Childcare

```html
<!DOCTYPE html>
<html lang="en">
<head>
<meta charset="utf-8">
<title>Twirl 'n' Hop poster</title>
<link rel="stylesheet" href="https://fonts.googleapis.com/css2?family=Chicle&family=Delius&family=Arimo:wght@700&display=swap">
<style>
  :root {
    --backdrop: #777b7e;
    --sky-top: #7cc8f0;
    --sky-bottom: #f4f9fb;
    --title: #2d1f78;
    --headline: #1f9a45;
    --pink: #e0157f;
    --orange: #f08a1d;
    --purple: #8d1f8f;
    --red: #e0224f;
    --blue: #1aa0d8;
    --navy: #2b2a6e;
    --ink: #222;
    --footer: #555;
    --hill-green: #9fd163;
    --hill-pale: #e6f08a;
    --art-yellow: #f6dc72;
    --art-orange: #ee8a3c;
    --art-red: #d9533a;
  }
  * { margin: 0; padding: 0; box-sizing: border-box; }
  html, body { width: 1200px; height: 1000px; overflow: hidden; background: var(--backdrop); }
  .poster {
    position: absolute; left: 312px; top: 92px; width: 576px; height: 814px;
    background: linear-gradient(180deg, var(--sky-top) 0%, #c5e6f6 40%, var(--sky-bottom) 70%);
    overflow: hidden;
  }
  .hills { position: absolute; left: 0; top: 0; }
  .title {
    position: absolute; top: 8px; width: 100%; text-align: center;
    font-family: "Chicle", cursive; font-weight: 400; font-size: 64px; line-height: 76px;
    color: var(--title); letter-spacing: 3px;
  }
  .headline {
    position: absolute; top: 96px; left: 8px; width: 560px; text-align: center;
    font-family: "Delius", cursive; font-size: 23px; line-height: 28px; color: var(--headline);
  }
  .pill { color: #fff; border-radius: 8px; padding: 0 3px; }
  .pill--pink { background: var(--pink); }
  .pill--orange { background: var(--orange); }
  .pill--purple { background: var(--purple); }
  .dancer {
    position: absolute; left: 24px; top: 190px; width: 250px; height: 400px;
    border-radius: 24px;
    background: linear-gradient(160deg, var(--art-yellow) 0%, var(--art-orange) 55%, var(--art-red) 100%);
  }
  .blurb {
    position: absolute; left: 262px; top: 173px; width: 290px; text-align: center;
    font-family: "Delius", cursive; font-size: 9.6px; line-height: 12.5px; color: var(--ink);
  }
  .callout { position: absolute; font-family: "Arimo", sans-serif; font-weight: 700; font-size: 13.5px; line-height: 19px; }
  .callout--price { left: 328px; top: 486px; color: var(--red); }
  .callout--trial { left: 334px; top: 513px; color: var(--purple); }
  .callout--intro { left: 270px; top: 562px; width: 258px; text-align: right; color: var(--blue); }
  .themes {
    position: absolute; left: 0; top: 661px; width: 100%; text-align: center;
    font-family: "Arimo", sans-serif; font-weight: 700; font-size: 11.8px; line-height: 16px; color: var(--navy);
    letter-spacing: .2px;
  }
  .footer {
    position: absolute; top: 790px; font-family: "Arimo", sans-serif; font-weight: 700; font-size: 13px; color: var(--footer);
  }
  .footer--phone { left: 17px; }
  .footer--email { right: 20px; }
</style>
</head>
<body>
<main class="poster">
  <svg class="hills" width="576" height="814" viewBox="0 0 576 814" aria-hidden="true">
    <ellipse cx="300" cy="900" rx="540" ry="360" fill="var(--hill-green)"/>
    <path d="M260 814 C 360 700, 500 660, 576 650 L576 814 Z" fill="var(--hill-pale)" opacity=".85"/>
    <path d="M0 814 C 120 760, 300 760, 420 814 Z" fill="#c4e27a" opacity=".7"/>
  </svg>

  <h1 class="title">TWIRL 'N' HOP</h1>

  <p class="headline">"Does you child love to <span class="pill pill--pink">dance,</span> <span class="pill pill--orange">sing</span> or <span class="pill pill--purple">play sport</span>?<br>Why not enrol in our fun filled program?"</p>

  <div class="dancer" role="img" aria-label="Illustration of a happy blonde girl dancing on a green hill with music notes and small children playing"></div>

  <p class="blurb">Twirl 'n' Hop offers little boys and girls a range of FUN classes, held in your childcare centre, that will introduce them to the wonderful world of music, movement and P.E.<br>Every class is a magical place to be with funky music, props, puppets, costumes and exciting equipment! Children will develop a range of skills including balance, co-ordination, confidence, motor skills, creativity, rhythm and much more!!<br>Each fortnight there is a different theme where children can express themselves and explore many dance genres as well as yoga, gymnastics, sport, musical instruments and ball skills. Detailed information on each class will be emailed to you every fortnight so you'll always be kept up-to-date with what your child is learning!! Twirl 'n' Hop also offers birthday parties!!!<br>You can select any of the themes listed, or we can custom make a party to the interest of your child. Your host will come dressed as a character of your choice and keep the children entertained for 1-2hrs.<br>Email us for more information!!</p>

  <p class="callout callout--price">"From only $10.00 per class"</p>
  <p class="callout callout--trial">"Sign up for your FREE<br>trial class today"</p>
  <p class="callout callout--intro">"A fun introduction<br>to the joy of Dance, Sport<br>and Music for 2-6yr olds.<br>Held in your childcare centre!!"</p>

  <p class="themes">· Jumping Jellybeans · Under the Sea · Superheros · Jungle Jam · Movie Magic<br>
  Balancing Bugs · Gymnastics and Rhythmic Gymnastics · Disco Divas and Singing Superstars<br>
  Hawaiian Holiday · Circus · Space · Bowling and Ball Skills · Colours and Shapes<br>
  Monsters · Magical Fairytales · Sport and Cheerleading · Mexican Fiesta<br>
  Animals · Aboriginal Adventure · Its Party Time</p>

  <p class="footer footer--phone">Phone: 0400 555 218</p>
  <p class="footer footer--email">Email: hello@twirlnhop.com.au</p>
</main>
</body>
</html>
```